looking for sleek business card to standout from the crowd!

We are a young biotechnology company looking to help you personalize your health through understanding your genetic make up. We need you help in making a clean but sleek business card design using our new logo. The goal? Any time we give our cards out, people say "nice card!" The feel we are going for is "modern-techy". We don't want to come across as an old, giant pharma company, but not trying to be a hipster either.

Target Market(s)

healthcare and biotechnology industry.

Industry/Entity Type

Biotechnology

Contact Information for Business Card

Info to include on the card will be NAME, TITLE, EMAIL, PHONE. The companies website (www.corvalinbio.com) should also be on the card some where. Would like the logo, when printed, to be raised.

Requirements
Must have
• The logo we have attached in the color it is in. Fonts for text should lean toward more professional/tech.
Nice to have
• Prefer white/light color background
Should not have
• cartoons, landscape backgrounds images.

```html
<!DOCTYPE html>
<html lang="en">
<head>
<meta charset="utf-8">
<title>Corvalin Business Card</title>
<link rel="stylesheet" href="https://fonts.googleapis.com/css2?family=Exo+2:wght@400;600;700&display=swap">
<style>
  :root {
    --brand-blue: #1a6cb5;
    --deep-blue: #14579a;
    --brand-green: #7dbb35;
    --ink: #4a4a4a;
    --card-white: #ffffff;
    --card-shade: #eef0f1;
    --backdrop: #2b2b2d;
  }
  html, body {
    margin: 0;
    padding: 0;
    width: 1200px;
    height: 1000px;
    overflow: hidden;
    background: var(--backdrop);
    font-family: "Exo 2", sans-serif;
  }
  .card {
    position: absolute;
    left: 100px;
    top: 214px;
    width: 1000px;
    height: 572px;
    border-radius: 26px;
    overflow: hidden;
    background: linear-gradient(135deg, var(--card-white) 40%, var(--card-shade) 100%);
    box-shadow: 0 18px 40px rgba(0,0,0,0.45);
  }
  .card-bands {
    position: absolute;
    left: 0;
    top: 0;
    width: 1000px;
    height: 572px;
  }
  .holder-name {
    position: absolute;
    left: 70px;
    top: 78px;
    margin: 0;
    font-size: 36px;
    line-height: 44px;
    font-weight: 700;
    letter-spacing: 1px;
    color: var(--brand-blue);
  }
  .holder-name .surname { color: var(--brand-green); }
  .holder-title {
    position: absolute;
    left: 70px;
    top: 124px;
    margin: 0;
    font-size: 23px;
    line-height: 30px;
    font-weight: 400;
    color: var(--ink);
    letter-spacing: 0.5px;
  }
  .contact-list {
    position: absolute;
    left: 70px;
    top: 168px;
    margin: 0;
    padding: 0;
    list-style: none;
    font-size: 21px;
    color: var(--ink);
  }
  .contact-list li {
    display: flex;
    align-items: center;
    height: 34px;
  }
  .contact-list svg {
    width: 18px;
    height: 18px;
    margin-right: 18px;
    fill: var(--deep-blue);
  }
  .contact-list .web-domain { color: var(--brand-blue); }
  .divider {
    position: absolute;
    left: 0;
    top: 300px;
    width: 1000px;
    height: 3px;
    background: var(--brand-green);
  }
  .brand {
    position: absolute;
    right: 70px;
    top: 172px;
    margin: 0;
    font-size: 64px;
    line-height: 76px;
    font-weight: 700;
    color: var(--brand-blue);
    letter-spacing: 2px;
  }
  .address {
    position: absolute;
    right: 70px;
    top: 340px;
    margin: 0;
    text-align: right;
    font-size: 22px;
    line-height: 32px;
    font-style: normal;
    color: var(--ink);
  }
</style>
</head>
<body>
  <section class="card">
    <svg class="card-bands" viewBox="0 0 1000 572" aria-hidden="true">
      <path fill="var(--brand-green)" d="M0,536 L350,536 C395,536 405,486 450,484 L1000,484 L1000,572 L0,572 Z"/>
      <path fill="var(--brand-blue)" d="M0,548 L362,548 C405,548 415,498 460,496 L1000,496 L1000,572 L0,572 Z"/>
    </svg>

    <h1 class="holder-name">AREN <span class="surname">DULAINE</span></h1>
    <p class="holder-title">CEO &amp; FOUNDER</p>

    <ul class="contact-list">
      <li>
        <svg viewBox="0 0 24 24"><path d="M6.6 10.8a15 15 0 0 0 6.6 6.6l2.2-2.2a1 1 0 0 1 1-.25 11.4 11.4 0 0 0 3.6.57 1 1 0 0 1 1 1V20a1 1 0 0 1-1 1A17 17 0 0 1 3 4a1 1 0 0 1 1-1h3.5a1 1 0 0 1 1 1c0 1.25.2 2.45.57 3.57a1 1 0 0 1-.25 1z"/></svg>
        +000 123 456 789
      </li>
      <li>
        <svg viewBox="0 0 24 24"><path d="M2 5h20v14H2z M3 6l9 7 9-7" fill="none" stroke="var(--deep-blue)" stroke-width="2"/></svg>
        yourname@email.com
      </li>
      <li>
        <svg viewBox="0 0 24 24"><circle cx="12" cy="12" r="10"/><path d="M2 12h20M12 2c3 3 3 17 0 20M12 2c-3 3-3 17 0 20" fill="none" stroke="#fff" stroke-width="1.5"/></svg>
        <span>www.<span class="web-domain">corvalinbio</span>.com</span>
      </li>
    </ul>

    <p class="brand">CORVALIN</p>

    <div class="divider"></div>

    <address class="address">Your Street Address,<br>Singapore, 1234</address>
  </section>
</body>
</html>
```